Commercial Real Estate

We need a business card design for a new commercial real estate business that specializes in apartment building brokerage. Not individual units but the entire complex. We find and represent the owners existing buildings and well as new buyers for those buildings. The design should convey trust, integrity, knowledge and growth. It should be easily read.

Target Market(s)

40 to 65 years old

Industry/Entity Type

Real Estate

```html
<!DOCTYPE html>
<html lang="en">
<head>
<meta charset="utf-8">
<title>Talvera Property Investments – Business Card</title>
<link rel="stylesheet" href="https://fonts.googleapis.com/css2?family=Roboto:wght@300;400;700&display=swap">
<style>
  :root {
    --canvas: #e4e2de;
    --teal: #5fa9a9;
    --teal-line: #5aa6a6;
    --card-white: #ececec;
    --ink: #4a5354;
    --ink-soft: #5d6566;
  }
  * { margin: 0; padding: 0; box-sizing: border-box; }
  html, body {
    width: 1200px; height: 900px; overflow: hidden;
    background: var(--canvas);
    font-family: "Roboto", Arial, sans-serif;
  }
  .canvas { position: relative; width: 1200px; height: 900px; }

  .card {
    position: absolute; top: 304px;
    width: 510px; height: 292px;
    box-shadow: 0 2px 6px rgba(0,0,0,0.12);
  }
  .card--front { left: 60px; background: var(--teal); }
  .card--back { left: 630px; background: var(--card-white); }

  .brand {
    position: absolute; display: flex; align-items: center; gap: 10px;
    color: var(--ink); font-weight: 700; white-space: nowrap;
  }
  .brand__square { width: 14px; height: 14px; background: var(--ink); }
  .card--front .brand { left: 50%; top: 50%; transform: translate(-50%, -50%); font-size: 22px; letter-spacing: 0.5px; }
  .card--back .brand { right: 30px; top: 34px; font-size: 15px; letter-spacing: 0.3px; }

  .person { position: absolute; left: 36px; top: 104px; color: var(--ink-soft); }
  .person__name { font-size: 22px; font-weight: 300; }
  .person__role { font-size: 11px; font-weight: 400; letter-spacing: 0.5px; margin-left: 10px; text-transform: uppercase; }

  .contacts { position: absolute; left: 36px; top: 144px; list-style: none; font-size: 12.5px; font-weight: 300; color: var(--ink-soft); line-height: 16px; }
  .contacts__key { display: inline-block; width: 14px; color: var(--teal); font-weight: 700; }

  .address { position: absolute; left: 36px; top: 204px; font-size: 12.5px; font-weight: 300; color: var(--ink-soft); }
  .divider { position: absolute; left: 36px; top: 232px; width: 250px; height: 2px; background: var(--teal-line); }
  .website { position: absolute; left: 36px; top: 244px; font-size: 13px; font-weight: 700; color: var(--ink); }
</style>
</head>
<body>
<main class="canvas">
  <section class="card card--front" aria-label="Card front">
    <div class="brand"><span class="brand__square"></span>Talvera Property Investments</div>
  </section>

  <section class="card card--back" aria-label="Card back">
    <div class="brand"><span class="brand__square"></span>Talvera Property Investments</div>
    <p class="person"><span class="person__name">Daniel Hartley</span><span class="person__role">Manager</span></p>
    <ul class="contacts">
      <li><span class="contacts__key">T</span>0400 555 218</li>
      <li><span class="contacts__key">F</span>0400 555 219</li>
      <li><span class="contacts__key">E</span>daniel.hartley@talvera.com</li>
    </ul>
    <p class="address">PO Box 2741 Riverton NT 0190</p>
    <div class="divider"></div>
    <p class="website">www.talvera.com</p>
  </section>
</main>
</body>
</html>
```